Swimming NC License Plate

I am a board representative of a not for profit organization that builds swimming pools, teaches swimming lessons and coaches a swim team. We would like a license plate designed with our mission core values of aquatics and swimming in mind. I have uploaded the graphic/template that the design must fit within. The Grey area on the template is where the graphics should fit.

I’ve now uploaded some samples of other plates.

Target Market(s)

Swimmers, swim coaches

Requirements
Must have
• Looking for a pool water element
• Since this will be printed on a license plate, I do not think that complex graphics will come out looking good. Few colors, simple themes.
Nice to have
• Lane lines / racing lines / simple swimmer graphics. Focus on competitive swimmings, and not recreational / back yard pools. Focus on competition pool or swimming.
• “SWIMMING” across the top of the plate.
Should not have
• Fish.

```html
<!DOCTYPE html>
<html lang="en">
<head>
<meta charset="utf-8">
<title>Swimming NC License Plate</title>
<link rel="stylesheet" href="https://fonts.googleapis.com/css2?family=Roboto:wght@700;900&display=swap">
<style>
  :root {
    --ink: #231f20;
    --paper: #ffffff;
    --pool-deep: #2fb0e0;
    --pool-light: #8fd8f2;
    --deck: #6b3a36;
    --badge-navy: #0b5c9c;
    --badge-teal: #3ba4c0;
    --stamp-grey: #e6e7e8;
  }
  html, body {
    margin: 0;
    padding: 0;
    width: 1200px;
    height: 619px;
    overflow: hidden;
    background: var(--paper);
  }
  .plate {
    position: relative;
    width: 1200px;
    height: 619px;
    overflow: hidden;
    background: var(--paper);
    font-family: "Roboto", Arial, sans-serif;
    color: var(--ink);
  }
  .pool-photo {
    position: absolute;
    left: 0;
    top: 0;
    width: 850px;
    height: 619px;
    background:
      linear-gradient(135deg, var(--deck) 0%, var(--deck) 18%, #c9b99a 18.5%, #d8d4cc 23%, transparent 24%),
      linear-gradient(90deg, var(--pool-deep) 0%, var(--pool-light) 72%, rgba(255,255,255,0) 100%);
  }
  .plate-title {
    position: absolute;
    left: 584px;
    top: 76px;
    margin: 0;
    font-size: 22px;
    font-weight: 700;
    line-height: 1;
    letter-spacing: 0.15px;
    white-space: nowrap;
  }
  .sticker-area {
    position: absolute;
    left: 1009px;
    top: 31px;
    width: 152px;
    height: 114px;
    background: var(--stamp-grey);
  }
  .number-area {
    position: absolute;
    left: 431px;
    top: 152px;
    width: 748px;
    height: 328px;
    background: var(--paper);
    border: 2px solid var(--ink);
    border-radius: 2px;
  }
  .amenity-badges {
    position: absolute;
    left: 84px;
    top: 240px;
  }
  .state-name {
    position: absolute;
    left: 94px;
    top: 478px;
    margin: 0;
    font-size: 125px;
    font-weight: 900;
    line-height: 1;
    letter-spacing: -1.8px;
    white-space: nowrap;
  }
</style>
</head>
<body>
  <main class="plate">
    <div class="pool-photo" role="img" aria-label="Overhead photo of a pool ladder, tiled deck edge and clear blue pool water"></div>

    <svg class="amenity-badges" width="316" height="160" viewBox="0 0 316 160" role="img" aria-label="Eight round pool amenity pictograms: swimsuit, life ring, swimmer, sunbather, shower, pool ladder, parasol, towel">
      <g stroke="var(--paper)" stroke-width="5">
        <circle cx="40"  cy="40"  r="36" fill="var(--badge-navy)"/>
        <circle cx="118" cy="40"  r="36" fill="var(--badge-teal)"/>
        <circle cx="195" cy="40"  r="36" fill="var(--badge-navy)"/>
        <circle cx="272" cy="40"  r="36" fill="var(--badge-teal)"/>
        <circle cx="40"  cy="117" r="36" fill="var(--badge-teal)"/>
        <circle cx="118" cy="117" r="36" fill="var(--badge-navy)"/>
        <circle cx="195" cy="117" r="36" fill="var(--badge-teal)"/>
        <circle cx="272" cy="117" r="36" fill="var(--badge-navy)"/>
      </g>
    </svg>

    <h1 class="plate-title">SWIMMING NC LICENSE PLATE</h1>
    <div class="sticker-area" aria-hidden="true"></div>
    <div class="number-area" aria-hidden="true"></div>
    <p class="state-name">NORTH CAROLINA</p>
  </main>
</body>
</html>
```